Brochure for Community-Based Therapy Company

Will be given out to patients, doctors, case managers. We are redesigning our marketing materials and would like a design for a brochure. We provide therapy to individuals who have been injured in car accidents or on the job. We provide occupational therapy, speech therapy and psychotherapy. We would like the brochure to utilize our corporate ID and color scheme that we are using for our other materials (see attached letterhead and logo).

Stock photos that are used should stay away from images of outpatient or hospital settings, stay away from photos with obvious disabilities (wheelchairs, learning to walk, etc), and nothing that looks like physical therapy, as we don't provide physical therapy only OT, Speech and psychotherapy. Would prefer to not have people wearing masks, as we will use this beyond the pandemic. Also, our staff wears business casual clothing so would prefer photos that the individuals are not wearing scrubs or other medical attire (lab coats, etc).

Target Market(s)

Patients, Physicians/Doctors, Case Managers

Industry/Entity Type

Healthcare

Requirements
Must have
• Prefer a booklet format but doesn't have to be 8.5 inch by 11 inch (can be a little smaller).

```html
<!DOCTYPE html>
<html lang="en">
<head>
<meta charset="utf-8">
<title>Larkfield Therapy Group – Therapy Brochure</title>
<link rel="stylesheet" href="https://fonts.googleapis.com/css2?family=Jost:ital,wght@0,400;0,500;0,700;0,800;1,400&family=Merriweather:ital,wght@0,300;0,400;1,300&display=swap">
<style>
:root{
  --backdrop:#d9d9d9;
  --paper:#ffffff;
  --green:#5f8f69;
  --green-deep:#5a8a64;
  --green-soft:#7c9e88;
  --ink:#3b3b3b;
  --blob:#e7ebe8;
  --photo-dark:#5d5c62;
}
*{box-sizing:border-box;margin:0;padding:0}
html,body{width:1200px;height:2520px;overflow:hidden;background:var(--backdrop)}
body{position:relative;font-family:"Merriweather",Georgia,serif;color:var(--ink)}
.page{position:absolute;background:var(--paper);overflow:hidden}
.cover{left:75px;top:71px;width:525px;height:745px}
.spread{left:75px;width:1050px;height:743px}
.spread-a{top:887px}
.spread-b{top:1703px}
.abs{position:absolute}
.body-copy{font-weight:300;font-size:12.6px;line-height:17.6px;color:var(--ink)}
.body-copy p+p{margin-top:17px}
.lead{color:var(--green-soft);font-weight:400}
.heading{font-family:"Jost",sans-serif;font-size:32px;line-height:34px;letter-spacing:1px;color:var(--green-soft);text-transform:uppercase;font-weight:400}
.heading b{color:var(--ink);font-weight:800}
/* cover */
.brand{position:absolute;left:32px;top:58px;display:flex;align-items:center;gap:8px;font-family:"Jost",sans-serif;font-weight:500;font-size:17px;color:var(--green);letter-spacing:.5px;line-height:19px}
.brand .dot{width:12px;height:12px;border-radius:50%;background:var(--green)}
.cover-title{position:absolute;right:62px;top:448px;text-align:right;font-family:"Jost",sans-serif;font-size:39px;line-height:45px;color:var(--ink);font-weight:400;text-transform:uppercase}
.cover-title b{color:#fff;font-weight:800}
/* spread a */
.bubble{position:absolute;border-radius:50%;background:rgba(95,143,105,.93);color:#fff;text-align:center;display:flex;flex-direction:column;align-items:center}
.bubble h3{font-family:"Jost",sans-serif;font-weight:400;font-size:15px;line-height:17px;letter-spacing:.5px}
.bubble h3 b{font-weight:700}
.bubble p{font-weight:300;font-size:12.4px;line-height:17.6px;margin-top:12px}
.who-we-are{left:49px;top:522px;width:430px;color:#fff}
.who-we-are h3{font-family:"Jost",sans-serif;font-weight:400;font-size:15px;letter-spacing:.5px;margin-bottom:9px}
.who-we-are p{font-weight:300;font-size:12.4px;line-height:17.6px}
.quote{left:52px;top:493px;width:185px;border-left:1px solid var(--green-soft);padding-left:11px;font-style:italic;font-weight:300;font-size:12.6px;line-height:20px;color:var(--green-soft)}
.list{list-style:none;margin-top:6px}
.list li{position:relative;padding-left:22px;margin-bottom:3px}
.list li::before{content:"•";position:absolute;left:0;font-size:9px}
.sub{font-family:"Merriweather",serif;color:var(--green-soft);font-size:13px;font-weight:400;margin-top:8px}
</style>
</head>
<body>

<section class="page cover">
  <svg class="abs" width="525" height="745" viewBox="0 0 525 745" style="left:0;top:0">
    <defs>
      <linearGradient id="coverPhoto" x1="0" y1="0" x2="1" y2="1">
        <stop offset="0" stop-color="#dfe7de"/>
        <stop offset=".5" stop-color="#b9cdb8"/>
        <stop offset="1" stop-color="#8fb39a"/>
      </linearGradient>
    </defs>
    <path role="img" aria-label="Photo of a woman stretching her neck, toned in soft green" fill="url(#coverPhoto)"
      d="M380 0 C330 60 280 100 270 150 C255 210 120 250 100 300 C80 350 110 380 95 410 C70 460 60 520 80 560 C90 620 60 660 80 745 L525 745 L525 0 Z"/>
    <path fill="var(--green-deep)"
      d="M360 0 L392 0 C340 70 300 110 290 160 C275 225 140 260 120 305 C100 350 130 385 115 415 C90 465 82 520 100 560 C112 620 85 670 104 745 L72 745 C52 665 70 615 62 565 C45 520 50 460 75 410 C90 380 62 350 82 295 C105 235 240 200 252 145 C262 95 315 55 360 0 Z"/>
  </svg>
  <div class="brand"><span class="dot"></span><span>LARKFIELD<br>THERAPY GROUP</span></div>
  <h1 class="cover-title">Your<br>Complete<br>Guide<br>to <b>High<br>Quality<br>Therapy</b></h1>
</section>

<section class="page spread spread-a">
  <div class="abs" role="img" aria-label="Photo of a woman wearing a neck brace, darkened grey tone"
       style="left:0;top:0;width:525px;height:743px;background:linear-gradient(120deg,#75737a 0%,var(--photo-dark) 45%,#48474d 100%)"></div>
  <div class="bubble" style="left:55px;top:46px;width:240px;height:240px;padding:34px 44px 0">
    <h3>MISSION<br><b>STATEMENT</b></h3>
    <p>Our mission is to provide high quality therapy that allows the people we serve to achieve an optimal level of functioning and to improve their quality of life.</p>
  </div>
  <div class="bubble" style="left:206px;top:211px;width:266px;height:266px;padding:30px 36px 0">
    <h3>VISION<br><b>STATEMENT</b></h3>
    <p style="margin-top:10px">To be a recognized leader in functional rehabilitation to individuals with a variety of diagnoses in the home and community-based setting with an emphasis on goal-directed individual rehabilitation for addressing safety, skill building, independence, and cognitive and physical recovery.</p>
  </div>
  <div class="abs who-we-are">
    <h3>WHO <b>WE ARE</b></h3>
    <p>For over 25 years, our company has been using evidence-based principles of rehabilitation to assist patients with their recovery. We are out in the real world with patients every day, helping them to get their lives back. Our goal is to provide functional home and community-based therapy to provide patient-centered holistic therapy with a state-of-the-art approach. Using the patient’s natural environment such as their home, community or workplace allows us to attain measurable outcomes that turn even small successes into something bigger.</p>
  </div>

  <svg class="abs" width="525" height="743" viewBox="0 0 525 743" style="left:525px;top:0">
    <path fill="var(--blob)" d="M240 0 C250 40 300 70 330 100 C400 140 420 230 400 300 C380 360 460 380 525 370 L525 0 Z"/>
  </svg>
  <h2 class="abs heading" style="left:573px;top:47px">Finding success in<br>the <b>rehabilitative<br>process relies</b><br>on certain key<br>factors</h2>
  <div class="abs" role="img" aria-label="Photo of a therapist guiding an older man through an exercise"
       style="left:824px;top:125px;width:226px;height:226px;border-radius:50%;border:2px solid var(--green-soft);background:linear-gradient(135deg,#eef2f5,#c9d3dc 55%,#8a95a0)"></div>
  <div class="abs body-copy" style="left:573px;top:247px;width:202px">
    <p><span class="lead">Getting to Know You:</span> We do not set goals that are important to us, but rather, we set goals that are important to you. We take input from you, and the people you trust like your physician, case manager or perhaps a trusted family member to identify your needs and then make a plan that is best suited for success.</p>
    <p><span class="lead">Comprehensive Evaluation:</span><br>We begin with an in-depth assessment with comprehensive evaluation protocols to determine your current level of functioning and how it compares to your prior level of functioning. We can then identify the areas that have been impacted and begin addressing them.</p>
    <p><span class="lead">Creating and Implementing a Customized Rehabilitation Plan:</span><br>After the evaluation protocols are</p>
  </div>
  <div class="abs body-copy" style="left:786px;top:375px;width:218px">
    <p>completed, a system of long-term and short-term goals are developed using our team approach. This allows for therapy to be tailored to your individual needs. A plan of care is developed and implemented based on your goals and the results of the evaluation.</p>
    <p style="margin-top:14px"><span class="lead">Focus on Accomplishments (Breaking Down Success):</span> In order to facilitate progress toward patient goals, our therapy is most effective with consistent therapy appointments and repetition across therapy disciplines, which maximizes carry over outside of therapy.</p>
  </div>
</section>

<section class="page spread spread-b">
  <svg class="abs" width="1050" height="743" viewBox="0 0 1050 743" style="left:0;top:0">
    <path fill="var(--blob)" d="M0 0 L55 0 C40 40 20 60 0 66 Z"/>
    <path fill="var(--blob)" d="M270 0 L770 0 C790 120 760 240 640 290 C560 320 420 310 340 250 C280 200 300 120 270 0 Z"/>
    <path fill="var(--blob)" d="M1050 450 C1000 470 960 560 990 620 C1000 680 960 720 940 743 L1050 743 Z"/>
    <circle role="img" aria-label="Image of brain scan slices in blue tones" cx="524" cy="50" r="223" fill="#2f4c5a"/>
    <circle cx="524" cy="50" r="223" fill="none" stroke="#47707f" stroke-width="2"/>
  </svg>
  <h2 class="abs heading" style="left:49px;top:48px">Why our<br>approach to<br><b>brain injury</b><br>is unique</h2>
  <div class="abs body-copy" style="left:49px;top:194px;width:192px">
    <p>In more traditional therapy settings such as programs using outpatient models, attempts are made to simulate functional activities, combined with more structured tasks, all performed within their clinic environment. However, the inability to generalize learning has been shown to be a reoccurring difficulty for individuals with Traumatic Brain Injury and can often manifest in cognitive inflexibility, which makes carryover of their learned skills to the real world, a challenge.</p>
  </div>
  <blockquote class="abs quote">“At Larkfield Therapy Group we are committed to helping people recover their cognitive, physical and psychosocial abilities following brain injury through intensive individual treatment which focuses on safety, skill building and increasing independence, community reintegration, and overall life satisfaction.”</blockquote>
  <div class="abs body-copy" style="left:262px;top:282px;width:222px">
    <p>Community-based treatment circumvents this difficulty by conducting therapy in the person’s home, school, workplace, or other settings within their community, such as a grocery store or at a post office. Clinicians are therefore able to witness first hand where a task is experiencing success or breaking down and can structure treatment accordingly. This allows for greater natural development of functional skills, with generalization issues no longer an obstacle toward meeting treatment goals.</p>
    <p>At Larkfield Therapy Group we are committed to helping people recover their cognitive, physical and psychosocial abilities following brain injury through intensive individual treatment which focuses on safety, skill building and increasing</p>
  </div>
  <div class="abs body-copy" style="left:573px;top:286px;width:160px">
    <p>independence, community reintegration, and overall life satisfaction. Our treatment approach is two-fold, with emphasis not only on direct restoration of brain functions, but also on helping the individual learn compensatory strategies (e.g., internal mnemonics, organizational systems, self-cuing techniques) or acquire assistive devices (e.g., planners, electronic reminders). Such methods are designed to reduce the effects of real-world disability when there is enduring cognitive impairment, and are most effective when introduced within a person’s own relevant environments.</p>
  </div>
  <h2 class="abs heading" style="left:762px;top:48px">Who<br><b>we serve</b></h2>
  <div class="abs body-copy" style="left:762px;top:128px;width:265px">
    <p>We treat adults and adolescents with a variety of diagnoses. We service home and community locations throughout Southeast and mid-Michigan.</p>
    <p style="margin-top:6px">Our therapists hold a variety of certifications and endorsements including CBIS (Certified Brain Injury Specialist), NeuroStim, and VoiceBoost.</p>
    <h4 class="sub">Diagnoses can include:</h4>
    <ul class="list">
      <li>Traumatic Brain Injury</li>
      <li>Postconcussional Syndrome</li>
      <li>Spinal Cord Injury</li>
      <li>Post-traumatic Stress Disorder</li>
      <li>Depression</li>
      <li>Anxiety</li>
      <li>Mood Disorders</li>
      <li>Musculoskeletal/Orthopedic injuries (ie. Spinal fractures/pathology, nerve injuries, pain)</li>
      <li>Visual Impairments</li>
      <li>Balance Disorders</li>
      <li>Movement Disorders</li>
      <li>Neuromuscular Pathologies</li>
      <li>Dysphagia</li>
    </ul>
    <h4 class="sub" style="font-size:14px;margin-top:10px">Funding Sources include:</h4>
    <ul class="list" style="margin-top:9px">
      <li>No-Fault Auto Insurance</li>
      <li>Workers Compensation Insurance</li>
      <li>Some Commercial Health Insurance Carriers</li>
    </ul>
  </div>
</section>

</body>
</html>
```